Syndicated consumer advocate seeks cool and creative web design

I'd like to collaborate with a web designer-artist to help me reimagine my web presence, Marowbeckfield.com. I publish my syndicated news articles on this site and collect email addresses for my weekly email newsletter. I want to maintain the current minimalist look and feel -- simple, uncluttered, intuitive -- while evolving it to the next level of functionality.

I take my inspiration from several nonprofit organizations and news sites. Those include 714, the Lantern Ledger, and CivisWatch. I want to use those sites as my leitmotif for the new theme, while also adopting some of their features.

Here's more about me: https://marowbeckfield.com/about-dorian-beckfield/

NOTE: Please be as creative as you want with your suggestions. I can handle it! I love outside-the-box thinking.

Target Market(s)

North American consumers.

Industry/Entity Type

News

Coding

Coded - Design and coding required

Number of Pages Required

2 page

Font styles to use
Sans Serif

Colors

Designer to choose only greyscale colors for use in the design.

Requirements
Must have
• The new theme should be visually appealing and very fast.

I'm looking for the ability to determine a "lead" story and control the content of other story boxes on the front page.

I don't mind using a starter theme such as Bracketry (I'm using that for the current version). However, I would prefer to not use an out-of-the-box news theme and simply modify it. I would like the coding to be watertight and error-free and hope to achieve console scores in the 90s.
Nice to have
• I like harmony, balance and Zen. I would like all the elements, including text, ads and social icons to look as if they are built with purpose and thought. It might be necessary to re-imagine or re-interpret the logo.
Should not have
• Please, no sliders. No bulky coding. No animations. No bright colors.

```html
<!DOCTYPE html>
<html lang="en">
<head>
<meta charset="utf-8">
<title>Marowbeckfield — News</title>
<link href="https://fonts.googleapis.com/css2?family=Open+Sans:wght@300;400;600;700&display=swap" rel="stylesheet">
<style>
:root{
  --black:#000;
  --ink:#111;
  --text:#1a1a1a;
  --muted:#8a8a8a;
  --line:#d9d9d9;
  --panel:#eeeeee;
  --card-panel:#f2f2f2;
  --hero-panel:#6b6b6b;
  --band:#3a3a3a;
  --footer:#1c1c1c;
  --accent:#5a5a5a;
  --accent-dark:#141414;
  --white:#fff;
}
*{box-sizing:border-box;margin:0;padding:0}
html,body{width:1200px;height:2753px;overflow:hidden}
body{position:relative;font-family:"Open Sans",Arial,sans-serif;color:var(--text);background:var(--white)}
ul,ol{list-style:none}

/* header */
.site-header{position:absolute;left:0;top:0;width:1200px;height:67px;background:var(--black)}
.brand{position:absolute;left:166px;top:20px;display:flex;align-items:center;gap:8px;color:var(--white);font-weight:700;font-size:17px}
.brand-square{width:14px;height:14px;background:var(--white)}
.main-nav{position:absolute;left:477px;top:21px;display:flex;gap:47px}
.main-nav a{color:var(--white);text-decoration:none;font-size:13px}
.btn-login,.btn-signup{position:absolute;top:11px;height:38px;width:106px;display:flex;align-items:center;justify-content:center;font-size:14px}
.btn-login{left:823px;border:1px solid var(--white);color:var(--white)}
.btn-signup{left:936px;background:var(--accent);color:var(--white);font-weight:600}

/* hero */
.hero{position:absolute;left:0;top:67px;width:1200px;height:372px;background:linear-gradient(180deg,#2d2d2d 0%,#1f1f1f 55%,#262626 100%)}
.hero-card{position:absolute;left:158px;top:65px;width:886px;height:252px;display:flex}
.hero-photo{width:385px;height:100%;background:radial-gradient(ellipse at 50% 60%,#b9a595 0%,#cfdde3 45%,#e6f2f6 80%)}
.hero-copy{flex:1;background:var(--hero-panel);color:var(--white);padding:48px 36px 0}
.hero-byline{font-size:11px;margin-bottom:6px}
.hero-title{font-size:20px;font-weight:600;line-height:25px;margin-bottom:12px}
.hero-text{font-size:15px;line-height:19.5px;max-width:370px}

/* stories */
.story-columns{position:absolute;left:169px;top:457px;display:flex;gap:7px}
.story-column{width:191px;display:flex;flex-direction:column;gap:9px}
.story-card{border:1px solid var(--line);background:var(--white);height:496px;overflow:hidden}
.story-card.long{height:580px}
.story-media{height:140px}
.story-body{padding:14px 9px 18px}
.story-date{font-size:11.5px;margin-bottom:9px}
.story-title{font-size:15.5px;font-weight:700;line-height:20px;white-space:nowrap;margin-bottom:13px}
.story-excerpt{font-size:12.6px;line-height:19.5px;color:var(--muted);padding:0 1px;letter-spacing:-.1px}

/* sidebar */
.sidebar{position:absolute;left:765px;top:457px;width:277px}
.recent-box{background:var(--panel);height:595px;padding:14px 7px 0}
.search-form{display:flex;gap:5px;margin-bottom:25px}
.search-input{width:201px;height:38px;background:var(--white);border:1px solid var(--line);display:flex;align-items:center;padding-left:16px;gap:8px;font-size:13px;color:#555}
.search-btn{width:56px;height:38px;background:var(--accent);color:var(--white);font-size:13px;font-weight:600;display:flex;align-items:center;justify-content:center}
.sidebar-heading{font-size:15px;font-weight:400;color:#555;margin:0 0 10px 0}
.recent-item{display:flex;gap:9px;height:123px}
.recent-thumb{width:85px;height:68px;flex:none;margin-top:6px}
.recent-title{font-size:15.5px;font-weight:700;line-height:20px;white-space:nowrap}
.recent-excerpt{font-size:13px;line-height:19.5px;color:var(--muted);padding-left:2px;margin-top:3px}

.popular-box{margin-top:8px;border:1px solid var(--line);height:486px}
.popular-box .sidebar-heading{margin:20px 0 0 15px}
.popular-tabs{display:flex;gap:8px;margin:19px 0 10px 15px}
.tab{height:35px;width:108px;border:1px solid #444;font-size:14px;display:flex;align-items:center;justify-content:center}
.tab-active{font-weight:600;color:var(--ink)}
.tab-idle{border-color:#aaa;color:#777}
.popular-list li{display:flex;gap:14px;height:76px;padding:13px 0 0 18px;border-bottom:1px solid var(--line);font-size:15.5px;line-height:20px}
.popular-list li:last-child{border-bottom:0}
.popular-list .num{font-weight:700;padding-top:3px}

.feature-card{margin-top:10px;border:1px solid var(--line);background:var(--card-panel);height:412px}
.feature-card .story-media{height:200px}
.feature-card .story-body{padding:20px 11px}

/* newsletter */
.digest{position:absolute;left:0;top:2187px;width:1200px;height:138px;background:var(--band)}
.digest-title{position:absolute;left:158px;top:48px;color:var(--white);font-size:25px;font-weight:600;white-space:nowrap}
.digest-input{position:absolute;left:639px;top:46px;width:291px;height:49px;background:var(--white);font-size:13px;color:#555;display:flex;align-items:center;padding-left:13px}
.digest-btn{position:absolute;left:930px;top:46px;width:112px;height:49px;background:var(--accent-dark);color:var(--white);font-size:13.5px;font-weight:700;display:flex;align-items:center;justify-content:center}

/* footer */
.site-footer{position:absolute;left:0;top:2325px;width:1200px;height:428px;background:var(--footer);color:var(--white)}
.footer-col{position:absolute;top:70px}
.footer-heading{font-size:17px;font-weight:600;margin-bottom:16px}
.footer-links li{font-size:15px;height:31px;color:#e6e6e6}
.trending li{display:flex;gap:12px;font-size:15px;line-height:20px;height:50px}
.trending .num{font-weight:700;padding-top:4px}
.social li{display:flex;align-items:center;gap:24px}
.social-dot{width:11px;height:11px;border-radius:50%;background:var(--white);margin-left:2px}
.copyright{position:absolute;left:0;width:1200px;top:366px;text-align:center;font-size:15px;color:#e6e6e6}
</style>
</head>
<body>

<header class="site-header">
  <div class="brand"><span class="brand-square"></span>Marowbeckfield</div>
  <nav class="main-nav"><a href="#">HOME</a><a href="#">NEWS</a><a href="#">NEWSLETTER</a></nav>
  <a class="btn-login">Log In</a>
  <a class="btn-signup">Sign Up</a>
</header>

<section class="hero">
  <div class="hero-card">
    <div class="hero-photo" role="img" aria-label="Portrait of the lead story's subject against a pale blue backdrop"></div>
    <div class="hero-copy">
      <p class="hero-byline">BY SELENA VARGA UPDATED: 3 HOURS AGO</p>
      <h1 class="hero-title">Long established fact that a<br>reader will &nbsp; the readable content of a page</h1>
      <p class="hero-text">There are many variations of passages of Lorem Ipsum available, but the majority have suffered alteration in some form, by injected humour,</p>
    </div>
  </div>
</section>

<main class="story-columns">
  <div class="story-column">
    <article class="story-card">
      <div class="story-media" role="img" aria-label="Overhead view of people working at laptops on a wooden table" style="background:linear-gradient(135deg,#6d5a44,#3d3934 60%,#8a7b69)"></div>
      <div class="story-body"><p class="story-date">MARCH 5, 2021</p><h3 class="story-title">Long established fact<br>that a reader</h3><p class="story-excerpt">Many desktop publishing packages and web page editors now use Lorem Ipsum as their default model text,and a search for 'lorem ipsum' will uncover many web sites still in their infancy. Various versions have evolved over the years, sometimes by accident, sometimes on purpose (injected humour and the like . . .</p></div>
    </article>
    <article class="story-card long">
      <div class="story-media" role="img" aria-label="Hands holding a glowing light bulb in the dark" style="background:radial-gradient(circle at 50% 55%,#a88345 0%,#3b3a36 45%,#1d2730 100%)"></div>
      <div class="story-body"><p class="story-date">MARCH 5, 2021</p><h3 class="story-title">Long established fact<br>that a reader</h3><p class="story-excerpt">Many desktop publishing packages and web page editors now use Lorem Ipsum as their default model text,and a search for 'lorem ipsum' will uncover many web sites still in their infancy. Various versions have evolved over the years, sometimes by accident, sometimes on purpose (injected humour and the likeThere are many variations of passages of Lorem Ipsum available, but the majority have suffered alteration in some form</p></div>
    </article>
    <article class="story-card">
      <div class="story-media" role="img" aria-label="Desk seen from above with laptops, notebooks and coffee" style="background:linear-gradient(135deg,#b9aa98,#8e8377 50%,#c7bcae)"></div>
      <div class="story-body"><p class="story-date">MARCH 5, 2021</p><h3 class="story-title">Long established fact<br>that a reader</h3><p class="story-excerpt">Many desktop publishing packages and web page editors now use Lorem Ipsum as their default model text,and a search for 'lorem ipsum' will uncover many web sites still in their infancy. Various versions have evolved over the years, sometimes by accident, sometimes on purpose (injected humour and the like . . .</p></div>
    </article>
  </div>

  <div class="story-column">
    <article class="story-card long">
      <div class="story-media" role="img" aria-label="Rows of red shopping carts beneath green plants" style="background:linear-gradient(180deg,#6f7d55 0%,#8b3a33 55%,#a42e2a 100%)"></div>
      <div class="story-body"><p class="story-date">MARCH 5, 2021</p><h3 class="story-title">Long established fact<br>that a reader</h3><p class="story-excerpt">Many desktop publishing packages and web page editors now use Lorem Ipsum as their default model text,and a search for 'lorem ipsum' will uncover many web sites still in their infancy. Various versions have evolved over the years, sometimes by accident, sometimes on purpose (injected humour and the likeThere are many variations of passages of Lorem Ipsum available, but the majority have suffered alteration in some form</p></div>
    </article>
    <article class="story-card">
      <div class="story-media" role="img" aria-label="Busy café interior with hanging lights" style="background:linear-gradient(180deg,#3a3b38,#6b6a60 50%,#2c2a26)"></div>
      <div class="story-body"><p class="story-date">MARCH 5, 2021</p><h3 class="story-title">Long established fact<br>that a reader</h3><p class="story-excerpt">Many desktop publishing packages and web page editors now use Lorem Ipsum as their default model text,and a search for 'lorem ipsum' will uncover many web sites still in their infancy. Various versions have evolved over the years, sometimes by accident, sometimes on purpose (injected humour and the like . . .</p></div>
    </article>
    <article class="story-card long">
      <div class="story-media" role="img" aria-label="Team meeting around a long conference table" style="background:linear-gradient(135deg,#c9ccd0,#7d7670 55%,#4d4744)"></div>
      <div class="story-body"><p class="story-date">MARCH 5, 2021</p><h3 class="story-title">Long established fact<br>that a reader</h3><p class="story-excerpt">Many desktop publishing packages and web page editors now use Lorem Ipsum as their default model text,and a search for 'lorem ipsum' will uncover many web sites still in their infancy. Various versions have evolved over the years, sometimes by accident, sometimes on purpose (injected humour and the likeThere are many variations of passages of Lorem Ipsum available, but the majority have suffered alteration in some form</p></div>
    </article>
  </div>

  <div class="story-column">
    <article class="story-card">
      <div class="story-media" role="img" aria-label="Night street with lit shop signs" style="background:linear-gradient(180deg,#2b2b2e,#4b4a4c 50%,#1a1a1c)"></div>
      <div class="story-body"><p class="story-date">MARCH 5, 2021</p><h3 class="story-title">Long established fact<br>that a reader</h3><p class="story-excerpt">Many desktop publishing packages and web page editors now use Lorem Ipsum as their default model text,and a search for 'lorem ipsum' will uncover many web sites still in their infancy. Various versions have evolved over the years, sometimes by accident, sometimes on purpose (injected humour and the like . . .</p></div>
    </article>
    <article class="story-card">
      <div class="story-media" role="img" aria-label="Commuters walking through a bright station concourse" style="background:linear-gradient(180deg,#c8ced6,#6d7480 55%,#2e3440)"></div>
      <div class="story-body"><p class="story-date">MARCH 5, 2021</p><h3 class="story-title">Long established fact<br>that a reader</h3><p class="story-excerpt">Many desktop publishing packages and web page editors now use Lorem Ipsum as their default model text,and a search for 'lorem ipsum' will uncover many web sites still in their infancy. Various versions have evolved over the years, sometimes by accident, sometimes on purpose (injected humour and the like . . .</p></div>
    </article>
    <article class="story-card">
      <div class="story-media" role="img" aria-label="Glass office towers seen from below against the sky" style="background:linear-gradient(135deg,#1e2530,#3c4654 55%,#b8c3cc)"></div>
      <div class="story-body"><p class="story-date">MARCH 5, 2021</p><h3 class="story-title">Long established fact<br>that a reader</h3><p class="story-excerpt">Many desktop publishing packages and web page editors now use Lorem Ipsum as their default model text,and a search for 'lorem ipsum' will uncover many web sites still in their infancy. Various versions have evolved over the years, sometimes by accident, sometimes on purpose (injected humour and the like . . .</p></div>
    </article>
  </div>
</main>

<aside class="sidebar">
  <div class="recent-box">
    <div class="search-form">
      <div class="search-input">
        <svg width="13" height="13" viewBox="0 0 13 13" fill="none" stroke="#777" stroke-width="1.4"><circle cx="5.5" cy="5.5" r="4.3"/><path d="M8.7 8.7L12 12"/></svg>
        Search . . .
      </div>
      <div class="search-btn">Search</div>
    </div>
    <h2 class="sidebar-heading">RECENT ARTICLES</h2>
    <div class="recent-item">
      <div class="recent-thumb" role="img" aria-label="People working at laptops" style="background:linear-gradient(135deg,#6d5a44,#3d3934 60%,#8a7b69)"></div>
      <div><h3 class="recent-title">Long established fact<br>that a reader</h3><p class="recent-excerpt">Many desktop publishing packages and web page editors &nbsp;. .</p></div>
    </div>
    <div class="recent-item">
      <div class="recent-thumb" role="img" aria-label="Commuters in a station" style="background:linear-gradient(180deg,#c8ced6,#6d7480 55%,#2e3440)"></div>
      <div><h3 class="recent-title">Long established fact<br>that a reader</h3><p class="recent-excerpt">Many desktop publishing packages and web page editors &nbsp;. .</p></div>
    </div>
    <div class="recent-item">
      <div class="recent-thumb" role="img" aria-label="Hands holding a glowing bulb" style="background:radial-gradient(circle at 50% 55%,#a88345 0%,#3b3a36 45%,#1d2730 100%)"></div>
      <div><h3 class="recent-title">Long established fact<br>that a reader</h3><p class="recent-excerpt">Many desktop publishing packages and web page editors &nbsp;. .</p></div>
    </div>
    <div class="recent-item">
      <div class="recent-thumb" role="img" aria-label="Night street with shop signs" style="background:linear-gradient(180deg,#2b2b2e,#4b4a4c 50%,#1a1a1c)"></div>
      <div><h3 class="recent-title">Long established fact<br>that a reader</h3><p class="recent-excerpt">Many desktop publishing packages and web page editors &nbsp;. .</p></div>
    </div>
  </div>

  <div class="popular-box">
    <h2 class="sidebar-heading">MOST POPULAR STORIES</h2>
    <div class="popular-tabs"><div class="tab tab-active">Most Read</div><div class="tab tab-idle">Most Emailed</div></div>
    <ol class="popular-list">
      <li><span class="num">1.</span><span>It is a long established fact<br>that a reader</span></li>
      <li><span class="num">2.</span><span>It is a long established fact<br>that a reader</span></li>
      <li><span class="num">3.</span><span>It is a long established fact<br>that a reader</span></li>
      <li><span class="num">4.</span><span>It is a long established fact<br>that a reader</span></li>
      <li><span class="num">5.</span><span>It is a long established fact<br>that a reader</span></li>
    </ol>
  </div>

  <article class="feature-card">
    <div class="story-media" role="img" aria-label="Person writing notes beside a laptop" style="background:linear-gradient(135deg,#9aa1a8,#d6d8d9 50%,#7b8188)"></div>
    <div class="story-body"><p class="story-date">MARCH 5, 2021</p><h3 class="story-title">Long established fact<br>that a reader</h3><p class="story-excerpt">Many desktop publishing packages and web page editors now use Lorem Ipsum as their default model text,and a search for 'lorem ipsum' will uncover many web sites still in their infancy.</p></div>
  </article>
</aside>

<section class="digest">
  <h2 class="digest-title">Stay informed with the Daily Digest</h2>
  <div class="digest-input">Enter Your email</div>
  <div class="digest-btn">Sign Up</div>
</section>

<footer class="site-footer">
  <div class="footer-col" style="left:157px">
    <h4 class="footer-heading">Trending Now</h4>
    <ol class="trending">
      <li><span class="num">1.</span><span>It is a long established fact<br>that a reader</span></li>
      <li><span class="num">2.</span><span>It is a long established fact<br>that a reader</span></li>
      <li><span class="num">3.</span><span>It is a long established fact<br>that a reader</span></li>
    </ol>
  </div>
  <div class="footer-col" style="left:466px">
    <h4 class="footer-heading">Browse By Type</h4>
    <ul class="footer-links"><li>Long established</li><li>Many desktop</li><li>Long established</li><li>Many desktop</li><li>sometimes on purpose</li></ul>
  </div>
  <div class="footer-col" style="left:711px">
    <h4 class="footer-heading">Topics</h4>
    <ul class="footer-links"><li>Long established</li><li>Many desktop</li><li>Long established</li><li>Many desktop</li><li>sometimes on purpose</li></ul>
  </div>
  <div class="footer-col" style="left:937px">
    <h4 class="footer-heading">Social Media</h4>
    <ul class="footer-links social">
      <li><span class="social-dot"></span>Townsquare</li>
      <li><span class="social-dot"></span>Quickpost</li>
      <li><span class="social-dot"></span>Clipstream</li>
      <li><span class="social-dot"></span>Snapgallery</li>
      <li><span class="social-dot"></span>Workweb</li>
    </ul>
  </div>
  <p class="copyright">Copyright©2021Marowbeckfield , All Rights Reserved.</p>
</footer>

</body>
</html>
```